Commercial Refrigeration Service Company requires stylish and fresh looking flyer.

We need a flyer to hand out to new customers. It should have a photo and our branding, list all the services that are offered and our contact details.
We would like two flyers to be supplied, both identical though one offering a discount until July ( Half Price Service Fee ). The flyer should be clear, interesting and in similar colours to the branding package supplied.
Please look at our website for information about the services on offer:
www.brambo-cooling.com.au

Target Market(s)

Cafes, bars, restaurants, pubs ect.

Font styles to use
Other font styles liked:
• Font package provided

Colors
85cae6
ffffff
333333

Requirements
Must have
• - The photo provided.
• - The company logo.
• - Similar feel to the website & business card.
• - Smooth layout and clear to understand.
Should not have
• - No clunky badges or prints.

```html
<!DOCTYPE html>
<html lang="en">
<head>
<meta charset="utf-8">
<title>Brambo Cooling – Flyer</title>
<link href="https://fonts.googleapis.com/css2?family=Josefin+Sans:wght@400;600&family=Montserrat:wght@300;400;600&display=swap" rel="stylesheet">
<style>
:root{
  --brand-blue:#85cae6;
  --accent-blue:#5bc3ee;
  --ink:#333333;
  --white:#ffffff;
  --panel-grey:#9a9a9a;
  --footer-dark:#333333;
}
*{margin:0;padding:0;box-sizing:border-box}
html,body{width:891px;height:1200px;overflow:hidden;background:#e9e9e9}
.flyer{position:relative;width:891px;height:1200px;background:var(--white);font-family:'Montserrat',sans-serif;color:var(--ink)}
.hero-photo{position:absolute;left:0;top:0;width:891px;height:418px;
  background:linear-gradient(180deg,#a9c7de 0%,#c9d5dc 35%,#7f8489 60%,#5d6165 100%)}
.rule{position:absolute;left:0;width:891px;height:4px;background:var(--accent-blue)}
.intro{position:absolute;left:0;top:422px;width:891px;height:324px;
  background:linear-gradient(90deg,#dcdcdc 0%,#ffffff 25%,#ffffff 75%,#dcdcdc 100%)}
.brand-box{position:absolute;left:52px;top:27px;width:328px;height:87px;background:var(--accent-blue);
  display:flex;align-items:center;justify-content:center}
.brand-name{font-family:'Josefin Sans',sans-serif;font-weight:400;font-size:27px;letter-spacing:9px;color:var(--ink);padding-left:9px}
.headline{position:absolute;left:427px;top:22px;font-family:'Josefin Sans',sans-serif;font-weight:600;
  font-size:25px;line-height:33.5px;letter-spacing:2.6px;color:var(--ink)}
.tagline{position:absolute;left:427px;top:133px;font-family:'Montserrat',sans-serif;font-weight:600;
  font-size:19px;letter-spacing:1.4px;color:var(--accent-blue)}
.about{position:absolute;left:53px;top:194px;width:792px;font-size:15.6px;line-height:20px;font-weight:400;
  text-align:justify;color:var(--ink);letter-spacing:-.2px}
.services{position:absolute;left:0;top:750px;width:891px;height:333px;background:var(--panel-grey)}
.services-title{position:absolute;top:12px;width:100%;text-align:center;font-family:'Josefin Sans',sans-serif;
  font-weight:600;font-size:26px;letter-spacing:3px;color:var(--accent-blue)}
.divider{position:absolute;top:56px;height:1px;background:#d6d6d6}
.service{position:absolute;width:200px;margin-left:-100px;text-align:center;color:var(--white);font-size:12.5px}
.service svg{display:block;margin:0 auto 10px;stroke:var(--white);fill:none;stroke-width:2;stroke-linecap:round;stroke-linejoin:round}
.footer{position:absolute;left:0;top:1087px;width:891px;height:113px;background:var(--footer-dark)}
.offer{position:absolute;left:53px;top:1058px;width:329px;height:142px;background:var(--accent-blue);text-align:center;color:var(--white)}
.offer-lead{margin-top:25px;font-family:'Josefin Sans',sans-serif;font-size:18.5px;letter-spacing:3px;color:var(--white)}
.offer-dots{margin:16px auto 0;display:block}
.offer-main{margin-top:16px;font-family:'Josefin Sans',sans-serif;font-weight:600;font-size:18.5px;letter-spacing:3px;color:var(--ink)}
.contact{position:absolute;left:427px;top:1093px;color:var(--white);font-size:14px;letter-spacing:2px;line-height:21px}
.contact .web{margin-top:12px;color:var(--accent-blue);font-weight:600;letter-spacing:3.6px}
</style>
</head>
<body>
<div class="flyer">
  <div class="hero-photo" role="img" aria-label="Photo of the technician standing beside the branded company service ute by the beach"></div>
  <div class="rule" style="top:418px"></div>

  <section class="intro">
    <div class="brand-box"><span class="brand-name">BRAMBO COOLING</span></div>
    <h1 class="headline">COMMERCIAL REFRIGERATION<br>&amp; ELECTRICAL SERVICES.<br>ICE MAKERS &amp; BEER SYSTEMS</h1>
    <p class="tagline">24 Hr Service, Sales &amp; Installations</p>
    <p class="about">Brambo Cooling is a company based in Eastern Sydney, providing commercial refrigeration and electrical services. Dan and his team believe in developing tight relationships with their clients and keeping things simple by offering a personalised service - speak to the same people and see the same faces. Brambo is completely paperless and uses cloud based trade service software to build a complete profile of your venue and equipment, allowing Dan to offer tailored advice for your business.</p>
  </section>

  <div class="rule" style="top:746px"></div>

  <section class="services">
    <h2 class="services-title">OUR SERVICES</h2>
    <div class="divider" style="left:199px;width:224px"></div>
    <div class="divider" style="left:468px;width:226px"></div>

    <div class="service" style="left:142px;top:92px">
      <svg width="40" height="64" viewBox="0 0 40 64"><path d="M10 6a6 6 0 0 1 12 0v34a11 11 0 1 1-12 0z"/><circle cx="16" cy="49" r="5"/><path d="M16 44V16M28 14h7M28 21h5M28 28h7M28 35h5"/></svg>
      Commercial Refrigeration</div>
    <div class="service" style="left:349px;top:92px">
      <svg width="50" height="64" viewBox="0 0 50 64"><path d="M4 4h42l-5 56H9z"/><path d="M6 18h38"/><rect x="15" y="24" width="11" height="11"/><rect x="25" y="32" width="11" height="11"/><rect x="14" y="40" width="11" height="11"/></svg>
      Ice makers</div>
    <div class="service" style="left:554px;top:92px">
      <svg width="44" height="64" viewBox="0 0 44 64"><path d="M24 32L40 6l-4-3-18 26"/><path d="M4 30h20v14h-8v6H4z"/><path d="M28 44v6"/><path d="M28 54c-2 3-2 6 0 6s2-3 0-6z"/></svg>
      Beer Systems</div>
    <div class="service" style="left:761px;top:92px">
      <svg width="44" height="64" viewBox="0 0 44 64"><path d="M28 4L8 34h14l-8 26 24-34H24z"/></svg>
      Electrical</div>

    <div class="service" style="left:231px;top:196px">
      <svg width="58" height="54" viewBox="0 0 58 54"><path d="M10 4l8 8-4 4-8-8a9 9 0 0 0 12 12l26 26 4-4-26-26A9 9 0 0 0 10 4z"/><path d="M50 4l-22 22M26 30l-16 16a4 4 0 0 0 6 6l16-16M46 2l8 8"/></svg>
      24hr Service</div>
    <div class="service" style="left:450px;top:196px">
      <svg width="72" height="54" viewBox="0 0 72 54"><path d="M2 4h8l6 32h50l4-24H12"/><path d="M16 36l-2 8h52"/><circle cx="22" cy="48" r="4"/><circle cx="58" cy="48" r="4"/></svg>
      Sales</div>
    <div class="service" style="left:671px;top:196px">
      <svg width="60" height="54" viewBox="0 0 60 54"><path d="M4 14l10-10 42 42-10 6z"/><path d="M10 14l4-4M16 20l4-4M22 26l4-4M28 32l4-4"/><path d="M56 8l-4-4-44 42-2 6 6-2z"/></svg>
      Installations</div>
  </section>

  <div class="rule" style="top:1083px"></div>
  <footer class="footer"></footer>

  <aside class="offer">
    <p class="offer-lead">DISCOUNT UNTIL JULY</p>
    <svg class="offer-dots" width="64" height="10" viewBox="0 0 64 10" fill="none" stroke="#333" stroke-width="1.5"><path d="M8 1l4 4-4 4-4-4zM32 1l4 4-4 4-4-4zM56 1l4 4-4 4-4-4z"/></svg>
    <p class="offer-main">HALF PRICE SERVICE FEE</p>
  </aside>

  <address class="contact" style="font-style:normal">
    <div>DANIEL HARTLEY</div>
    <div>0400 281 746</div>
    <div>info@brambo-cooling.com.au</div>
    <div class="web">WWW.BRAMBO-COOLING.COM.AU</div>
  </address>
</div>
</body>
</html>
```